Business Card for new Architectural Firm

I intend to practice in a rural mountain community in upstate NY, focusing on residential and light commercial projects, including second home / vacation properties. I wish to convey a feeling of rural outdoorsy modernity.

Color is important - bold and urbane. Secondary or tertiary colors preferred.

Font is important, idiosyncratic is ok

Optionally, I may choose to use the name Brackenfold Studio. If used as part of your design, all of the Must Haves are still required.

Images uploaded are logos I like

Industry/Entity Type

Residential

Contact Information for Business Card

Caldwell Prusinski
Architect (This word should stand alone or be associated with my name - not license number)
NY License No. 582163
caldwell@designcpx.com
607 394 2858

Font styles to use
Sans Serif
Decorative

Requirements
Must have
• Whatever files I need to best utilize your design
• PDF
• JPG
• EPS
• Vectorwhatsit
Nice to have
• Logo or element that can be incorporated into other print material.
• Could be a font based card
Should not have
• no clip art
• No templates
• no floor plans
• no building photographs

```html
<!DOCTYPE html>
<html lang="en">
<head>
<meta charset="utf-8">
<title>Caldwell Prusinski, Architect: Business Card</title>
<link rel="stylesheet" href="https://fonts.googleapis.com/css2?family=Share+Tech+Mono&family=Space+Mono:wght@700&family=Didact+Gothic&display=swap">
<style>
  :root {
    --backdrop: #e9e6e2;
    --card: #4b3c42;
    --contact-orange: #d9792b;
    --name-green: #b2d47f;
    --guide-green: rgba(178, 212, 127, 0.45);
  }
  * { margin: 0; padding: 0; box-sizing: border-box; }
  html, body {
    width: 1200px;
    height: 800px;
    overflow: hidden;
    background: var(--backdrop);
  }
  .card {
    position: absolute;
    left: 75px;
    top: 100px;
    width: 1050px;
    height: 600px;
    background: var(--card);
    box-shadow: 0 12px 30px rgba(0, 0, 0, 0.25);
  }
  .contact {
    position: absolute;
    left: 330px;
    top: 70px;
    width: 560px;
    text-align: center;
    font-family: "Share Tech Mono", monospace;
    font-size: 30px;
    line-height: 1.2;
    letter-spacing: 0.14em;
    color: var(--contact-orange);
    text-transform: uppercase;
  }
  .name-guides {
    position: absolute;
    left: 0;
    top: 200px;
    width: 1050px;
    height: 130px;
  }
  .name {
    position: absolute;
    left: 28px;
    top: 212px;
    font-family: "Space Mono", monospace;
    font-weight: 700;
    font-size: 88px;
    line-height: 1;
    letter-spacing: 0.02em;
    color: var(--name-green);
    white-space: nowrap;
  }
  .title {
    position: absolute;
    left: 330px;
    top: 345px;
    font-family: "Didact Gothic", sans-serif;
    font-size: 46px;
    letter-spacing: 0.12em;
    color: var(--name-green);
  }
</style>
</head>
<body>
  <div class="card">
    <div class="contact">
      <p>NY License No. 582163</p>
      <p>caldwell@designcpx.com</p>
      <p>607 394 2858</p>
    </div>

    <svg class="name-guides" viewBox="0 0 1050 130" aria-hidden="true">
      <g stroke="var(--guide-green)" stroke-width="1">
        <line x1="10" y1="22" x2="1040" y2="22"/>
        <line x1="10" y1="30" x2="1040" y2="30"/>
        <line x1="10" y1="95" x2="1040" y2="95"/>
        <line x1="10" y1="103" x2="1040" y2="103"/>
      </g>
    </svg>

    <h1 class="name">Caldwell Prusinski</h1>
    <p class="title">Architect</p>
  </div>
</body>
</html>
```